Packaging design for high end, natural skin care line needed

Marisol Thackery Beauty needs a label design. It is a new skin care line I am launching.
For years my line Velvet Orchard Beauty was quite popular and featured in several magazines, but for personal reasons had to be shut down. Now I am launching a new line featuring VOB's top selling products, but focused solely on skin care more so than cosmetics. All products will still be handmade, but the line should still look professional-something worthy of a Brindle Market shelf!
I am branding it with my name, as I am often quoted in articles related to gluten in beauty products, so Marisol Thackery and beauty are key words.
The key products will be facial and body serums which are packaged in .5oz., 1oz. and larger amber glass bottles with black dropper tops, I will include pictures below. For dimensions, the labels can be any size that you think will work best, but need to at the least fit the 1oz. bottle, dimensions shown here http://www.corvelflask.example/amber-glass-tall-round-flask/p/QZ7K-93/
I loved the former VOB logo, but for Marisol Thackery Beauty I am looking for something more personal, more apothecary-like, and probably less colorful.
The line will be small, just a handful of products, but luxe, rich.
I am attaching photos of Velvet Orchard Beauty's packaging for your reference.
Thanks much!!

Hi Everyone! Thank you for your submissions! Please see the links I provided in the brief, I really am looking for something more technical looking, like an apothecary. And want black text on a white background, not a black background, and nothing flowery.
Thank you all!!
Marisol

Target Market(s)

My clients are primarily women of all ages, but with more of a skin care focus, and no longer a cosmetic one, I would also like to appeal to a male audience. My clients are health conscious, gluten-free, natural, paleo, or vegan, etc. Target age is probably 25-55. Products are a bit high end, priced $45-65.

Industry/Entity Type

Cosmetics

Requirements
Must have
• It must at least say Marisol Thackery, or can say Marisol Thackery Beauty, but "Beauty" is not necessary. And capitalization is open, try whatever you think serves the brand. Likely slogans or taglines that can be included but are not essential: Care for your skin. Love and care for your skin. Handmade with love in the USA. Handmade in the USA. Think modern day apothecary. Small batch scotch. Something fine, but custom, handmade.
Nice to have
• I like the aesthetic of Oribel Skin Care a bit http://www.oribelhollis.example.au/
And of Dorian Valtz as shown here http://www.pinboardia.example/pin/847302915563017442/
Also of something like this that is even customizable http://www.pinboardia.example/pin/58274106392285514/
Every product is handmade in small batches, with fine ingredients, a moderate price point of around $45-$65. And I will likely begin making custom orders. So there could be a space to say when it was made, or for whom. I would like to keep the colors classic though, I probably want to stay away from the bright pink on this one.
Should not have
• As I mentioned, probably want to stay away from a lot of color. I like black vs. gray for the text, as it will show up better in editorials. I must look good, but also photograph well. Thanks!

```html
<!DOCTYPE html>
<html lang="en">
<head>
<meta charset="utf-8">
<title>Marisol Thackery – Balancing Facial Serum Labels</title>
<link rel="stylesheet" href="https://fonts.googleapis.com/css2?family=Share+Tech+Mono&display=swap">
<style>
  :root {
    --canvas: #ffffff;
    --label-edge: #cfd0d2;
    --band: #e6e7e8;
    --bar: #d1d3d4;
    --brand-ink: #b1b2b4;
    --ink: #555658;
    --rule: #b8b9bb;
    --panel: #fdfdfd;
  }
  * { margin: 0; padding: 0; box-sizing: border-box; }
  html, body {
    width: 1200px; height: 1130px; overflow: hidden;
    background: var(--canvas);
    font-family: "Share Tech Mono", monospace;
    color: var(--ink);
  }
  .label {
    position: absolute; left: 22px; width: 1156px; height: 444px;
    background: #fff;
    border: 1px solid var(--label-edge);
    box-shadow: 0 0 5px rgba(0,0,0,0.18);
  }
  .label--classic { top: 22px; height: 442px; }
  .label--framed { top: 664px; }
  .text {
    position: absolute; left: 0; width: 100%; text-align: center; white-space: nowrap;
  }
  .tagline { font-size: 22px; letter-spacing: 3px; }
  .brand-name { font-size: 41px; letter-spacing: 3px; color: var(--brand-ink); }
  .product { font-size: 29px; letter-spacing: 6px; line-height: 40px; }
  .size { font-size: 28px; letter-spacing: 1px; }
  .rule {
    position: absolute; left: 68px; width: 1018px; height: 0;
    border-top: 1px dotted var(--rule);
  }
  .brand-band {
    position: absolute; left: 0; top: 61px; width: 100%; height: 106px;
    background: var(--band); border-top: 1px solid #d6d7d9;
  }
  .frame { position: absolute; left: 0; top: 0; }
  .brand-bar { position: absolute; left: 155px; top: 78px; width: 846px; height: 36px; background: var(--bar); }
  .brand-box { position: absolute; left: 359px; top: 62px; width: 439px; height: 106px; background: var(--band); }
</style>
</head>
<body>

<section class="label label--classic">
  <p class="text tagline" style="top:16px">CARE FOR YOUR SKIN</p>
  <div class="brand-band"></div>
  <p class="text brand-name" style="top:118px">Marisol Thackery</p>
  <p class="text product" style="top:187px">BALANCING<br>FACIAL SERUM</p>
  <div class="rule" style="top:319px"></div>
  <div class="rule" style="top:359px"></div>
  <p class="text size" style="top:394px">1oz</p>
</section>

<section class="label label--framed">
  <svg class="frame" width="1156" height="444" viewBox="0 0 1156 444" aria-hidden="true">
    <rect x="18.5" y="22.5" width="1117" height="400" fill="var(--panel)" stroke="#dcdddf"/>
    <path d="M19 23 H110 Q112 34 100 38 Q70 40 48 52 Q26 66 19 85 Z" fill="var(--band)"/>
    <path d="M1135 23 H1044 Q1042 34 1054 38 Q1084 40 1106 52 Q1128 66 1135 85 Z" fill="var(--band)"/>
  </svg>
  <p class="text tagline" style="top:30px">CARE FOR YOUR SKIN</p>
  <div class="brand-bar"></div>
  <div class="brand-box"></div>
  <p class="text brand-name" style="top:120px">Marisol Thackery</p>
  <p class="text product" style="top:189px">BALANCING<br>FACIAL SERUM</p>
  <div class="rule" style="top:321px"></div>
  <div class="rule" style="top:361px"></div>
  <p class="text size" style="top:389px">1oz</p>
</section>

</body>
</html>
```